Halvorn spray foam and Environmental

I have business cards but need new ones. The ones I have are very bland. Here is. Y company website http://www.halvornsprayfoam.ca

Also I can send you copies of the current cards
I would also need my current logo on the new design as well.. Also spray foam and Environmental

Industry/Entity Type

Business

Logo Text

Halvorn.

```html
<!DOCTYPE html>
<html lang="en">
<head>
<meta charset="utf-8">
<title>Halvorn Business Card</title>
<link href="https://fonts.googleapis.com/css2?family=Roboto:wght@400;500;700&display=swap" rel="stylesheet">
<style>
:root{
  --purple:#5c2a7a;
  --ink:#555459;
  --mark:#4a4c52;
  --card:#fbfbfb;
  --backdrop:#e4e4e6;
  --rule:#b9b9bc;
}
*{margin:0;padding:0;box-sizing:border-box}
html,body{width:1200px;height:1134px;overflow:hidden;background:var(--backdrop);font-family:'Roboto',sans-serif;color:var(--ink)}
.card{position:absolute;left:262px;width:675px;height:380px;background:var(--card);border-radius:12px;box-shadow:0 3px 8px rgba(0,0,0,.18)}
.card--front{top:162px}
.card--back{top:590px}
.brand-square{position:absolute;background:var(--mark)}
.brand-name{position:absolute;font-family:'Roboto',sans-serif;font-weight:700;color:var(--purple);letter-spacing:.5px;line-height:1}
.card--front .brand-square{left:108px;top:45px;width:67px;height:67px}
.card--front .brand-name{left:46px;top:127px;font-size:54px}
.division{position:absolute;top:236px}
.division--foam{left:49px}
.division--enviro{left:347px}
.division h2{font-size:26px;font-weight:500;color:var(--purple);letter-spacing:.3px;line-height:1;margin-bottom:18px}
.contact{list-style:none}
.contact li{display:flex;align-items:center;height:23px;font-size:15.5px}
.contact svg{width:16px;height:16px;margin-right:10px;fill:var(--purple)}
.divider{position:absolute;left:306px;top:240px;width:2px;height:103px;background:var(--rule)}
.card--back .brand-square{left:284px;top:34px;width:96px;height:79px}
.card--back .brand-name{left:0;right:0;top:131px;text-align:center;font-size:64px}
.services{position:absolute;top:207px;list-style:none;font-size:16px;text-transform:uppercase;letter-spacing:.2px}
.services li{height:27px;display:flex;align-items:center}
.services li::before,.services--right li::after{content:"";width:9px;height:9px;border-radius:50%;background:var(--purple)}
.services--left{left:38px}
.services--left li::before{margin-right:8px}
.services--right{right:38px;text-align:right}
.services--right li{justify-content:flex-end}
.services--right li::before{display:none}
.services--right li::after{margin-left:8px}
</style>
</head>
<body>
<section class="card card--front">
  <div class="brand-square"></div>
  <div class="brand-name">HALVORN</div>

  <div class="division division--foam">
    <h2>SPRAY FOAM</h2>
    <ul class="contact">
      <li><svg viewBox="0 0 16 16"><path d="M4 1l3 3-2 2c1 2 3 4 5 5l2-2 3 3-2 2C7 14 2 9 2 3z"/></svg>604 555 0142</li>
      <li><svg viewBox="0 0 16 16"><path d="M1 3h14v10H1zM2 4l6 5 6-5v1L8 10 2 5z" fill-rule="evenodd"/></svg>halvornfoam@mailbox.ca</li>
      <li><svg viewBox="0 0 16 16"><path d="M8 1a7 7 0 100 14A7 7 0 008 1zm0 1.5c.8 0 1.7 1.5 2 4H6c.3-2.5 1.2-4 2-4zM2.6 7.5H5c0 1 .1 1.7.2 2.5H3a5.5 5.5 0 01-.4-2.5zm8.4 0h2.4a5.5 5.5 0 01-.4 2.5h-2.2c.1-.8.2-1.5.2-2.5zM6 7.5h4c0 1-.1 1.8-.2 2.5H6.2C6.1 9.3 6 8.5 6 7.5zm.3 3.5h3.4c-.4 1.6-1 2.5-1.7 2.5s-1.3-.9-1.7-2.5z"/></svg>www.halvornsprayfoam.ca</li>
    </ul>
  </div>

  <div class="divider"></div>

  <div class="division division--enviro">
    <h2>ENVIRONMENTAL</h2>
    <ul class="contact">
      <li><svg viewBox="0 0 16 16"><path d="M4 1l3 3-2 2c1 2 3 4 5 5l2-2 3 3-2 2C7 14 2 9 2 3z"/></svg>604 555 0187</li>
      <li><svg viewBox="0 0 16 16"><path d="M1 3h14v10H1zM2 4l6 5 6-5v1L8 10 2 5z" fill-rule="evenodd"/></svg>halvornenviro@mailbox.ca</li>
      <li><svg viewBox="0 0 16 16"><path d="M8 1a7 7 0 100 14A7 7 0 008 1zm0 1.5c.8 0 1.7 1.5 2 4H6c.3-2.5 1.2-4 2-4zM2.6 7.5H5c0 1 .1 1.7.2 2.5H3a5.5 5.5 0 01-.4-2.5zm8.4 0h2.4a5.5 5.5 0 01-.4 2.5h-2.2c.1-.8.2-1.5.2-2.5zM6 7.5h4c0 1-.1 1.8-.2 2.5H6.2C6.1 9.3 6 8.5 6 7.5zm.3 3.5h3.4c-.4 1.6-1 2.5-1.7 2.5s-1.3-.9-1.7-2.5z"/></svg>www.halvornenvironmental.ca</li>
    </ul>
  </div>
</section>

<section class="card card--back">
  <div class="brand-square"></div>
  <div class="brand-name">HALVORN</div>

  <ul class="services services--left">
    <li>Roofing Foam</li>
    <li>Slabjacking</li>
    <li>2 Pound / Half Pound</li>
    <li>Sound Proofing</li>
    <li>Batt Insulation</li>
    <li>Attic Blow In</li>
  </ul>

  <ul class="services services--right">
    <li>Air Monitoring</li>
    <li>Asbestos Testing</li>
    <li>Asbestos Removal</li>
    <li>Building Demolition</li>
    <li>Lead Testing</li>
    <li>Mould Removal</li>
  </ul>
</section>
</body>
</html>
```